Personal Letterhead - Vintage / Antique - Foil Pressed

I need a personal letterhead. I'm an engineer and maker who enjoys writing letters and calligraphy. The final design will be foil pressed with either gold or copper foil. I'm going for an antique and vintage look. Something akin to Walter Brisbury's letterhead. Please include a spot for a web address and email, each are 16 characters long. The primary name to include is Daniel Whitlow. You can include print elements if desired that will be separate from the foil elements. At your discretion, you may or may not include the Whitlow signature I attached. It is optional depending on how well it meshes with your design.
I, explicitly, am not just looking for my name in gold or copper at the top of the page. I'm looking for additional design elements that give a similar feeling to the example design provided.

```html
<!DOCTYPE html>
<html lang="en">
<head>
<meta charset="utf-8">
<title>Daniel Whitlow — Personal Letterhead</title>
<link rel="stylesheet" href="https://fonts.googleapis.com/css2?family=Crimson+Pro:wght@700&family=Poppins:wght@300;400&display=swap">
<style>
  :root {
    --copper: #c47f55;
    --paper: #eae6e5;
    --ink: #231f20;
    --seal-grey: #9b9b9e;
  }
  * { margin: 0; padding: 0; box-sizing: border-box; }
  html, body { width: 1200px; height: 3053px; overflow: hidden; }
  body { background: var(--copper); position: relative; font-family: "Poppins", sans-serif; }

  .sheet {
    position: absolute; left: 25px; width: 1150px; height: 1489px;
    background: var(--paper);
  }
  .sheet--first { top: 25px; }
  .sheet--second { top: 1539px; }

  .sheet__art { position: absolute; inset: 0; width: 1150px; height: 1489px; }

  .name {
    position: absolute; left: 0; right: 0; top: 222px;
    text-align: center;
    font-family: "Crimson Pro", serif; font-weight: 700;
    font-size: 66px; line-height: 1; color: var(--ink); letter-spacing: 0.3px;
  }
  .tagline {
    position: absolute; left: 0; right: 0; top: 320px;
    text-align: center; font-size: 22px; font-weight: 400;
    color: var(--ink); line-height: 1;
  }
  .contact {
    position: absolute; top: 1370px;
    font-size: 14px; letter-spacing: 3px; color: var(--copper);
    line-height: 1; display: flex; align-items: center; gap: 10px;
  }
  .contact--web { right: 620px; }
  .contact--mail { left: 622px; }
  .contact__icon { width: 18px; height: 18px; }
</style>
</head>
<body>
<svg width="0" height="0" style="position:absolute">
  <defs>
    <g id="corner">
      <g fill="none" stroke="#c47f55" stroke-width="3">
        <path d="M55 287 V92 M92 55 H287"/>
        <path d="M67 202 V92 M92 67 H202"/>
      </g>
      <rect x="53" y="53" width="41" height="41" fill="#c47f55" opacity="0.35" role="img" aria-label="Fretwork corner ornament"/>
    </g>
    <g id="masthead">
      <path id="arc" d="M325 186 Q575 14 830 179" fill="none"/>
      <text font-family="Poppins, sans-serif" font-weight="300" font-size="26" letter-spacing="9" fill="#231f20">
        <textPath href="#arc" startOffset="50%" text-anchor="middle">FROM THE WORKSHOP OF</textPath>
      </text>
      <g stroke="#c47f55" fill="none">
        <path d="M272 192 H548 M602 192 H878" stroke-width="2"/>
        <circle cx="575" cy="192" r="16" stroke-width="6" stroke-dasharray="5 4.4"/>
        <circle cx="575" cy="192" r="15" stroke-width="2"/>
        <circle cx="575" cy="192" r="7" stroke-width="2"/>
        <path d="M272 305 H878" stroke-width="2"/>
      </g>
      <circle cx="985" cy="165" r="66" fill="#9b9b9e" opacity="0.35" role="img" aria-label="Quality guaranteed seal"/>
    </g>
    <rect id="quill" x="553" y="1355" width="42" height="46" rx="6" fill="#c47f55" opacity="0.3"/>
  </defs>
</svg>

<section class="sheet sheet--first">
  <svg class="sheet__art" viewBox="0 0 1150 1489">
    <use href="#corner"/>
    <use href="#corner" transform="translate(1150 0) scale(-1 1)"/>
    <use href="#corner" transform="translate(0 1489) scale(1 -1)"/>
    <use href="#corner" transform="translate(1150 1489) scale(-1 -1)"/>
    <use href="#masthead"/>
    <use href="#quill" role="img" aria-label="Quill pen emblem"/>
  </svg>
  <h1 class="name">DANIEL WHITLOW</h1>
  <p class="tagline">ENGINEER • MAKER</p>
  <p class="contact contact--web">WEBSITE: WWW.DANIEL.WHITLOW.PE</p>
  <p class="contact contact--mail">EMAIL: DANIEL@WHITLOW.PE</p>
</section>

<section class="sheet sheet--second">
  <svg class="sheet__art" viewBox="0 0 1150 1489">
    <use href="#corner"/>
    <use href="#corner" transform="translate(1150 0) scale(-1 1)"/>
    <use href="#corner" transform="translate(0 1489) scale(1 -1)"/>
    <use href="#corner" transform="translate(1150 1489) scale(-1 -1)"/>
    <use href="#masthead"/>
    <use href="#quill" role="img" aria-label="Quill pen emblem"/>
  </svg>
  <h1 class="name">DANIEL WHITLOW</h1>
  <p class="tagline">ENGINEER • MAKER</p>
  <p class="contact contact--web">
    <svg class="contact__icon" viewBox="0 0 18 18" fill="none" stroke="#c47f55" stroke-width="1.4">
      <circle cx="9" cy="9" r="7.5"/><ellipse cx="9" cy="9" rx="3.2" ry="7.5"/><path d="M1.5 9 H16.5"/>
    </svg>WWW.DANIEL.WHITLOW.PE</p>
  <p class="contact contact--mail">
    <svg class="contact__icon" viewBox="0 0 20 16" fill="none" stroke="#c47f55" stroke-width="1.4">
      <rect x="1" y="2" width="18" height="12"/><path d="M1 2 L10 9 L19 2"/>
    </svg>DANIEL@WHITLOW.PE</p>
</section>
</body>
</html>
```